8.5 x 8.5 Dale Morven Flyer

Wednesday Workouts
with
Dale Morven
@liftwithdalemorven
Sponsored by BRAMBLE CREST HOMES GROUP
Join us Virtually each Wednesday from 7 - 7:30 pm
email frontdesk@bramblecresthomes.example for Vidora Link
reserved for BCHG Agents and Special Invitees
BRAMBLE CREST HOMES
Phone (555) 618-2739

```html
<!DOCTYPE html>
<html lang="en">
<head>
<meta charset="utf-8">
<title>Wednesday Workouts with Dale Morven</title>
<link rel="stylesheet" href="https://fonts.googleapis.com/css2?family=Anton&family=Barlow+Condensed:wght@500;600&family=Catamaran:wght@600&family=Oswald:wght@600&display=swap">
<style>
  :root {
    --paper: #ffffff;
    --ink: #141414;
    --gold: #e6d77f;
    --white: #f4f4f4;
    --smoke-dark: #1c1c1c;
    --smoke-light: #5a5a5a;
  }
  html, body {
    margin: 0;
    padding: 0;
    width: 1200px;
    height: 1200px;
    overflow: hidden;
    background: var(--paper);
  }
  .flyer {
    position: relative;
    width: 1200px;
    height: 1200px;
    background: var(--paper);
    color: var(--white);
  }
  .flyer__panel {
    position: absolute;
    inset: 0;
    width: 1200px;
    height: 1200px;
  }
  .flyer__photo {
    position: absolute;
    left: 40px;
    top: 205px;
    width: 660px;
    height: 960px;
    background:
      radial-gradient(ellipse 55% 40% at 50% 45%, #6b4a36 0%, rgba(107,74,54,0.6) 45%, rgba(20,20,20,0) 75%),
      radial-gradient(ellipse 70% 25% at 45% 95%, var(--smoke-light) 0%, rgba(90,90,90,0) 70%),
      var(--smoke-dark);
    border-radius: 6px;
  }
  .flyer__content {
    position: absolute;
    right: 101px;
    top: 0;
    width: 1000px;
    text-align: right;
  }
  .title {
    position: absolute;
    right: 0;
    top: 72px;
    margin: 0;
    font-family: "Anton", "Oswald", sans-serif;
    font-weight: 400;
    font-size: 104px;
    line-height: 1;
    letter-spacing: 1px;
    color: var(--white);
    white-space: nowrap;
  }
  .host {
    position: absolute;
    right: 0;
    top: 204px;
    margin: 0;
    font-family: "Oswald", sans-serif;
    font-weight: 600;
    font-size: 64px;
    line-height: 1;
    color: var(--gold);
    font-variant: small-caps;
    white-space: nowrap;
  }
  .handle {
    position: absolute;
    right: 0;
    top: 290px;
    margin: 0;
    font-family: "Catamaran", sans-serif;
    font-weight: 600;
    font-size: 42px;
    line-height: 1;
    color: var(--white);
  }
  .info {
    position: absolute;
    right: 0;
    margin: 0;
    font-family: "Barlow Condensed", sans-serif;
    font-weight: 500;
    font-size: 36px;
    line-height: 41px;
    color: var(--white);
    white-space: nowrap;
  }
  .info .accent { color: var(--gold); }
  .info--join { top: 408px; }
  .join-heading {
    display: block;
    font-family: "Oswald", sans-serif;
    font-weight: 600;
    font-size: 44px;
    line-height: 60px;
    color: var(--gold);
    text-transform: uppercase;
  }
  .info--email { top: 584px; font-size: 33px; }
  .info--reserved { top: 750px; }
  .sponsor {
    position: absolute;
    right: 0;
    top: 904px;
    text-align: right;
  }
  .sponsor__label {
    font-family: "Catamaran", sans-serif;
    font-weight: 600;
    font-size: 22px;
    letter-spacing: 1px;
    color: var(--white);
  }
  .sponsor__name {
    margin-top: 26px;
    display: flex;
    align-items: center;
    justify-content: flex-end;
    gap: 12px;
    font-family: "Catamaran", sans-serif;
    font-weight: 600;
    font-size: 24px;
    letter-spacing: 1px;
    color: var(--white);
  }
  .sponsor__mark {
    width: 22px;
    height: 22px;
    background: var(--gold);
  }
  .phone {
    position: absolute;
    right: 0;
    top: 1064px;
    margin: 0;
    font-family: "Oswald", sans-serif;
    font-weight: 600;
    font-size: 42px;
    line-height: 1;
    color: var(--white);
    white-space: nowrap;
  }
  .phone .accent { color: var(--gold); font-variant: small-caps; }
</style>
</head>
<body>
<main class="flyer">
  <svg class="flyer__panel" viewBox="0 0 1200 1200" aria-hidden="true">
    <path fill="#141414" d="M32 22 L120 30 L210 18 L330 28 L460 20 L590 30 L720 18 L850 28 L980 20 L1090 30 L1150 18 L1172 24 L1166 120 L1178 240 L1168 380 L1180 520 L1170 660 L1178 800 L1166 940 L1176 1060 L1168 1150 L1160 1180 L1040 1172 L920 1182 L780 1172 L640 1182 L500 1172 L360 1180 L220 1172 L100 1182 L28 1176 L36 1060 L24 940 L34 800 L22 660 L32 520 L24 380 L34 240 L26 120 Z"/>
  </svg>

  <div class="flyer__photo" role="img" aria-label="Photo of the trainer in a dark tank top lifting a curl barbell, with grey smoke at his feet"></div>

  <div class="flyer__content">
    <h1 class="title">WEDNESDAY WORKOUTS</h1>
    <p class="host">With Dale Morven</p>
    <p class="handle">@liftwithdalemorven</p>

    <p class="info info--join">
      <span class="join-heading">Join Us</span>
      VIRTUALLY EACH<br>
      <span class="accent">WEDNESDAY</span> FROM 7 - 7:30 PM
    </p>

    <p class="info info--email">
      <span class="accent">EMAIL</span> frontdesk@bramblecresthomes.example<br>
      for Vidora Link
    </p>

    <p class="info info--reserved">
      <span class="accent">RESERVED FOR</span><br>
      BCHG Agents and Special Invitees
    </p>

    <div class="sponsor">
      <div class="sponsor__label">SPONSORED BY</div>
      <div class="sponsor__name"><span class="sponsor__mark"></span>BRAMBLE CREST HOMES</div>
    </div>

    <p class="phone"><span class="accent">Phone</span> (555) 618-2739</p>
  </div>
</main>
</body>
</html>
```